Overview:
We are seeking a talented graphic designer to create a cinematic and visually captivating movie poster for our upcoming romantic drama, "A Velvet Summer on Corsa". The poster must have a sense of elegance, romance, and the luxurious allure of a Mediterranean escape, while incorporating royal symbolism in a subtle yet sophisticated way.
✨ Design Goals & Style
Theme: Romantic, royal, dreamy, warm, and aspirational.
Setting: Ibiza beach with the sea and sun clearly visible, featuring a warm orange and pink sunset to set the romantic mood.
Colour Palette: Sunset tones – orange, pink, coral, soft golds, and sea blues.
Mood: Glamorous, heartfelt, summery, and regal.
📌 Key Visual Elements
Background:
Ibiza beach scene with sunset (orange & pink tones).
Ocean and horizon line in the distance.
Optionally include subtle silhouettes (e.g., palm trees or a royal yacht far out at sea).
Title Placement:
Movie title “A Velvet Summer on Corsa” should be placed at the top of the poster.
Include lead actor names "Delphine Marrow" and "Gregory Tillwand"
Use an elegant, serif or calligraphic typeface to match the romantic and royal theme.
Title Design Element:
Embed a crown graphic into the title—ideally integrated with one of the letters (like the "R" in "Royal" or "A") in a tasteful, balanced way.
We'll provide an example image to serve as reference for style.
Also:
A soft glow or lens flare effect from the sunset.
Silhouettes of a couple, subtle and not overpowering.
Space for billing block or release date at the bottom (placeholder text for now).
📎 Deliverables
Final movie poster in vertical format print-ready (CMYK, 300 dpi).
A web-optimized version (RGB, suitable for social media and website use).
Editable source file (Photoshop PSD or Illustrator AI).
Look and feel
Each slider illustrates characteristics of the customer's brand and the style your logo design should communicate.

```html
<!DOCTYPE html>
<html lang="en">
<head>
<meta charset="utf-8">
<title>A Velvet Summer on Corsa — Poster</title>
<link rel="stylesheet" href="https://fonts.googleapis.com/css2?family=Cinzel:wght@400;500;600&family=Oswald:wght@400&display=swap">
<style>
  :root {
    --stage: #5f5f5f;
    --sky-top: #6b3450;
    --sky-pink: #b84a4c;
    --sky-coral: #e2673a;
    --horizon: #f5963e;
    --sea: #b7522c;
    --sand: #4a1c14;
    --title: #f7d3a4;
    --names: #f4dcc0;
    --billing: #e9b37a;
  }
  * { margin: 0; padding: 0; box-sizing: border-box; }
  html, body {
    width: 1200px; height: 645px; overflow: hidden;
    background: var(--stage);
  }
  .poster {
    position: absolute;
    left: 400px; top: 22px;
    width: 400px; height: 600px;
    overflow: hidden;
  }
  .poster__scene {
    position: absolute; inset: 0;
    background:
      radial-gradient(circle at 63% 64%, rgba(255,220,140,.75) 0, rgba(255,170,80,.35) 9%, rgba(255,140,60,0) 28%),
      linear-gradient(180deg,
        var(--sky-top) 0%,
        var(--sky-pink) 22%,
        var(--sky-coral) 45%,
        var(--horizon) 66%,
        var(--sea) 70%,
        #8a3620 84%,
        var(--sand) 100%);
  }
  .credits {
    position: absolute; top: 22px; left: 55px; right: 66px;
    display: flex; justify-content: space-between;
    font-family: "Cinzel", serif; font-weight: 500;
    font-size: 14px; line-height: 18px; letter-spacing: .5px;
    color: var(--names);
  }
  .credits__name--right { text-align: right; }
  .title {
    position: absolute; top: 70px; left: 0; right: 0;
    text-align: center;
    font-family: "Cinzel", serif; font-weight: 500;
    color: var(--title);
    text-shadow: 0 2px 6px rgba(90,30,20,.35);
  }
  .title__line { display: block; line-height: 1; }
  .title__line--one { font-size: 56px; }
  .title__line--two { font-size: 56px; margin-top: 4px; }
  .title__line--three { font-size: 54px; margin-top: 4px; }
  .title__small { font-size: 22px; vertical-align: 14px; margin-right: 6px; }
  .billing {
    position: absolute; left: 0; right: 0; top: 556px;
    text-align: center;
    font-family: "Oswald", sans-serif;
    color: var(--billing);
    letter-spacing: .2px;
  }
  .billing__line { display: block; font-size: 6px; line-height: 11px; }
  .billing__line--main { font-size: 6.5px; }
</style>
</head>
<body>
  <main class="poster">
    <div class="poster__scene" role="img" aria-label="Sunset beach scene: pink and orange sky, glowing sun over the sea, palm fronds, a distant yacht and the silhouette of an embracing couple on the sand"></div>

    <header class="credits">
      <p class="credits__name">DELPHINE<br>MARROW</p>
      <p class="credits__name credits__name--right">GREGORY<br>TILLWAND</p>
    </header>

    <h1 class="title">
      <span class="title__line title__line--one"><span class="title__small">A</span>VELVET</span>
      <span class="title__line title__line--two">SUMMER</span>
      <span class="title__line title__line--three"><span class="title__small">ON</span>CORSA</span>
    </h1>

    <footer class="billing">
      <span class="billing__line">A SUNSET HOUSE PICTURE · A FILM BY LENA ORSO</span>
      <span class="billing__line billing__line--main">DELPHINE MARROW GREGORY TILLWAND IN A VELVET SUMMER ON CORSA · MUSIC BY ARLO VENN · EDITED BY MAE CORT · PRODUCED BY IDA RUSK</span>
    </footer>
  </main>
</body>
</html>
```